Poster Design Project

About Us
Brimco is a company that specializes in providing communication solutions to the travel market. Our simple vision of “every hotel should have a mobile phone in the guest rooms”, led us to develop a path breaking cost effective mobile phone. With full integration capabilities with the hotels property management system, location based marketing, user locator and other features, this product is unique in addressing the hospitality segment.
Product Placement
The Brimco mobile will be placed in the hotel room on an A4 Sized transparent stand (the transparent stand is attached for your reference. If you notice, the phone will be placed in the jacket on the bottom left and in another jacket on the bottom right will be the brochure. So effectively, the design space available on the A4 brochure is only 60% of the space). The designed poster that we wish designed will be inserted in the A4 sized acrylic stand. The stand would typically be on the bedside table or on the study table of the hotel room. The A4 design should be bright and vibrant in keeping with our logo colors.
Attached is our logo. Also attached is the symbol of our phone that could be used innovatively on the brochure if you think it helps.
Attached is the content for the poster.
Reason: Feedback from the management team got delayed, hence the extension. Thanks
Reason: The delay is in the content finalization.

```html
<!DOCTYPE html>
<html lang="en">
<head>
<meta charset="utf-8">
<title>Brimco in-room poster</title>
<link href="https://fonts.googleapis.com/css2?family=Fira+Sans:wght@500;600&display=swap" rel="stylesheet">
<style>
  :root {
    --orange: #f7a033;
    --orange-deep: #f26a21;
    --ink: #4b4b4d;
    --paper: #ffffff;
    --backdrop: #d6d6d6;
  }
  html, body {
    margin: 0;
    padding: 0;
    width: 1200px;
    height: 724px;
    overflow: hidden;
    background: var(--backdrop);
    font-family: "Fira Sans", Arial, sans-serif;
  }
  .poster {
    position: absolute;
    left: 390px;
    top: 44px;
    width: 420px;
    height: 636px;
    background: var(--paper);
    overflow: hidden;
  }
  .poster__bubbles {
    position: absolute;
    inset: 0;
  }
  .bubble { fill: var(--orange); }
  .bubble--deep { fill: var(--orange-deep); opacity: 0.75; }
  .header {
    position: absolute;
    left: 22px;
    top: 10px;
    display: flex;
    align-items: center;
    gap: 20px;
  }
  .brand-dot {
    width: 64px;
    height: 64px;
    border-radius: 50%;
    background: var(--paper);
    flex: none;
    margin-top: 22px;
  }
  .header__text {
    color: var(--paper);
    font-weight: 600;
    font-size: 22px;
    line-height: 26px;
    margin: 0;
  }
  .offer {
    position: absolute;
    left: 0;
    right: 0;
    top: 188px;
    margin: 0;
    padding: 0;
    list-style: none;
    text-align: center;
    color: var(--ink);
    font-weight: 600;
    font-size: 19px;
  }
  .offer__item { line-height: 28px; }
  .offer__plus {
    color: var(--orange);
    font-size: 28px;
    line-height: 29px;
    font-weight: 600;
  }
  .offer__price { line-height: 28px; }
  .offer__price .equals {
    color: var(--orange);
    font-size: 28px;
    margin-right: 4px;
  }
  .perks {
    position: absolute;
    left: 26px;
    top: 505px;
    margin: 0;
    width: 200px;
    color: var(--paper);
    font-weight: 500;
    font-size: 17px;
    line-height: 23px;
  }
</style>
</head>
<body>
  <main class="poster">
    <svg class="poster__bubbles" width="420" height="636" viewBox="0 0 420 636" aria-hidden="true">
      <rect class="bubble" x="0" y="0" width="420" height="100"/>
      <circle class="bubble" cx="20" cy="110" r="45"/>
      <circle class="bubble" cx="105" cy="125" r="50"/>
      <circle class="bubble" cx="195" cy="118" r="48"/>
      <circle class="bubble" cx="290" cy="108" r="52"/>
      <circle class="bubble" cx="375" cy="95" r="45"/>
      <circle class="bubble--deep" cx="45" cy="148" r="30"/>
      <circle class="bubble--deep" cx="330" cy="20" r="62"/>
      <circle class="bubble" cx="390" cy="102" r="24" opacity="0.9"/>

      <circle class="bubble" cx="60" cy="545" r="75"/>
      <circle class="bubble" cx="150" cy="525" r="60"/>
      <circle class="bubble" cx="238" cy="505" r="42"/>
      <rect class="bubble" x="0" y="560" width="280" height="76"/>
      <circle class="bubble" cx="255" cy="585" r="55"/>
      <circle class="bubble--deep" cx="238" cy="515" r="38"/>
      <circle class="bubble--deep" cx="65" cy="590" r="68"/>
    </svg>

    <header class="header">
      <span class="brand-dot"></span>
      <h1 class="header__text">Brimco<br>Pick up this phone NOW,<br>to keep talking...</h1>
    </header>

    <ul class="offer">
      <li class="offer__item">SAVE 80% on international roaming</li>
      <li class="offer__plus">+</li>
      <li class="offer__item">Get a LOCAL number</li>
      <li class="offer__plus">+</li>
      <li class="offer__item">60 FREE minutes of international Calls</li>
      <li class="offer__plus">+</li>
      <li class="offer__item">60 FREE minutes of local calls</li>
      <li class="offer__plus">+</li>
      <li class="offer__price"><span class="equals">=</span>499 BHT</li>
    </ul>

    <p class="perks">Itemized bill on checkout Flexible tariff plans to choose from Excellent call quality</p>
  </main>
</body>
</html>
```